New locally owned rental company needs a flyer to circulate

Need flyer with logo, phone# and address. We rent cars to anyone with driver's license and proper insurance. Rates as low as $50/day. Can offer compact cars, mid-size and full size sedans. Also SUV's.

```html
<!DOCTYPE html>
<html lang="en">
<head>
<meta charset="utf-8">
<title>DriveSoon Car &amp; Van Rental Flyer</title>
<link rel="stylesheet" href="https://fonts.googleapis.com/css2?family=Archivo+Black&family=Oswald:wght@600;700&family=Arimo:wght@400&display=swap">
<style>
  :root {
    --stage: #5f5f5f;
    --brand-blue: #1b4fa8;
    --band-blue: #1d55b8;
    --brand-green: #20a23a;
    --ink: #111111;
    --night: #000000;
    --paper: #ffffff;
  }
  html, body {
    margin: 0;
    width: 1200px;
    height: 2400px;
    overflow: hidden;
    background: var(--stage);
  }
  .flyer {
    position: absolute;
    left: 40px;
    top: 480px;
    width: 1120px;
    height: 1441px;
    box-shadow: 0 12px 30px rgba(0,0,0,.35);
  }
  .flyer svg { display: block; width: 100%; height: 100%; }
  .brand-name { font-family: "Archivo Black", sans-serif; fill: var(--brand-blue); }
  .brand-tagline { font-family: "Archivo Black", sans-serif; fill: var(--ink); letter-spacing: 9px; }
  .rate-lead { font-family: "Oswald", sans-serif; font-weight: 600; fill: var(--ink); }
  .rate-price { font-family: "Oswald", sans-serif; font-weight: 700; fill: var(--brand-green); }
  .offer-copy { font-family: "Arimo", sans-serif; fill: var(--paper); }
  .phone-number { font-family: "Oswald", sans-serif; font-weight: 700; fill: var(--paper); }
  .contact-line { font-family: "Arimo", sans-serif; fill: var(--paper); }
</style>
</head>
<body>
<div class="flyer">
  <svg viewBox="0 0 855 1100" xmlns="http://www.w3.org/2000/svg">
    <defs>
      <linearGradient id="sky" x1="0" y1="0" x2="0" y2="1">
        <stop offset="0" stop-color="#2f8ee0"/>
        <stop offset="0.55" stop-color="#9cc8ea"/>
        <stop offset="1" stop-color="#e9eef2"/>
      </linearGradient>
      <linearGradient id="studio" x1="0" y1="0" x2="0" y2="1">
        <stop offset="0" stop-color="#e6eef6"/>
        <stop offset="1" stop-color="#6f7f93"/>
      </linearGradient>
      <linearGradient id="roadside" x1="0" y1="0" x2="0" y2="1">
        <stop offset="0" stop-color="#8db8e0"/>
        <stop offset="0.5" stop-color="#5e6f82"/>
        <stop offset="1" stop-color="#c8c8c4"/>
      </linearGradient>
      <linearGradient id="redcar" x1="0" y1="0" x2="1" y2="1">
        <stop offset="0" stop-color="#8a0f1c"/>
        <stop offset="0.5" stop-color="#d22538"/>
        <stop offset="1" stop-color="#2a0408"/>
      </linearGradient>
      <linearGradient id="fadedcar" x1="0" y1="0" x2="1" y2="0">
        <stop offset="0" stop-color="#f1f1f1"/>
        <stop offset="0.5" stop-color="#fafafa"/>
        <stop offset="1" stop-color="#ececec"/>
      </linearGradient>
    </defs>

    <!-- base -->
    <rect class="canvas-night" width="855" height="1100" fill="var(--night)"/>

    <!-- white header sweep -->
    <path class="header-sweep" d="M0,0 H855 V150 C855,300 760,395 600,408 C420,420 210,385 0,300 Z" fill="var(--paper)"/>
    <rect class="header-photo" x="70" y="10" width="780" height="260" fill="url(#fadedcar)" opacity="0.8" role="img" aria-label="Faded photo of a white car behind the heading"/>

    <!-- green accent arcs -->
    <path class="accent-arc-left" d="M0,130 C0,215 25,270 62,300 L55,308 C18,285 -2,235 0,185 Z" fill="var(--brand-green)"/>
    <path class="accent-arc-right" d="M855,130 C858,240 810,310 712,335 L720,320 C800,290 842,225 846,150 Z" fill="var(--brand-green)"/>

    <!-- red car photo -->
    <rect class="photo-red-sedan" x="322" y="690" width="480" height="205" rx="90" fill="url(#redcar)" role="img" aria-label="Photo of a red compact sedan on a black reflective floor"/>

    <!-- main circle photo -->
    <circle class="photo-ring" cx="319" cy="457" r="287" fill="var(--brand-green)"/>
    <circle class="photo-main" cx="319" cy="457" r="278" fill="url(#sky)" role="img" aria-label="Photo of happy friends riding in a white convertible under a blue sky"/>

    <!-- SUV circle -->
    <circle class="photo-ring" cx="660" cy="533" r="124" fill="var(--brand-green)"/>
    <circle class="photo-ring-gap" cx="660" cy="533" r="116" fill="var(--night)"/>
    <circle class="photo-suv" cx="660" cy="533" r="110" fill="url(#studio)" role="img" aria-label="Photo of a silver-blue SUV in a showroom"/>

    <!-- sedan circle -->
    <circle class="photo-ring" cx="177" cy="755" r="132" fill="var(--brand-green)"/>
    <circle class="photo-ring-gap" cx="177" cy="755" r="124" fill="var(--paper)"/>
    <circle class="photo-sedan" cx="177" cy="755" r="118" fill="url(#roadside)" role="img" aria-label="Photo of a grey full-size sedan parked outdoors"/>

    <!-- heading -->
    <text class="brand-name" x="427" y="112" font-size="66" text-anchor="middle">DriveSoon</text>
    <text class="brand-tagline" x="427" y="152" font-size="27" text-anchor="middle">Car &amp; Van Rental</text>

    <!-- rates -->
    <text class="rate-lead" x="640" y="220" font-size="29" text-anchor="middle">Rates as low</text>
    <text class="rate-lead" x="640" y="246" font-size="29" text-anchor="middle">as</text>
    <text class="rate-price" x="640" y="300" font-size="46" text-anchor="middle">$50/day.</text>

    <!-- offer copy -->
    <text class="offer-copy" x="100" y="918" font-size="19.5">We rent cars to anyone with driver's license and proper insurance.</text>
    <text class="offer-copy" x="100" y="944" font-size="19.5">Can offer compact cars, mid-size and full size sedans. Also SUV's.</text>

    <!-- contact band -->
    <rect class="contact-band" x="0" y="1005" width="855" height="95" fill="var(--band-blue)"/>
    <polygon class="phone-tab" points="498,977 802,977 775,1030 477,1030" fill="var(--brand-green)"/>
    <g class="icon-phone" transform="translate(528,1003)">
      <circle r="17" fill="none" stroke="var(--paper)" stroke-width="3"/>
      <path d="M-8,-9 l5,-1 3,6 -3,3 c2,4 4,6 8,8 l3,-3 6,3 -1,5 c-12,1 -22,-9 -21,-21 z" fill="var(--paper)"/>
    </g>
    <text class="phone-number" x="565" y="1018" font-size="38">555-014-2270</text>

    <g class="icon-pin" transform="translate(92,1048)">
      <circle r="18" fill="none" stroke="var(--paper)" stroke-width="2.5"/>
      <path d="M0,12 C-8,2 -8,-3 -8,-4 A8,8 0 0 1 8,-4 C8,-3 8,2 0,12 Z" fill="none" stroke="var(--paper)" stroke-width="2.5"/>
      <circle cx="0" cy="-4" r="3" fill="var(--paper)"/>
    </g>
    <text class="contact-line" x="130" y="1042" font-size="18.5">address 4870B South Harbor Avenue</text>
    <text class="contact-line" x="130" y="1066" font-size="18.5">Riverton, AL 35999</text>

    <g class="icon-globe" transform="translate(525,1058)" fill="none" stroke="var(--paper)" stroke-width="2">
      <circle r="17"/>
      <circle r="11"/>
      <ellipse rx="5" ry="11"/>
      <line x1="-11" y1="0" x2="11" y2="0"/>
      <line x1="0" y1="-11" x2="0" y2="11"/>
    </g>
    <text class="contact-line" x="557" y="1065" font-size="18.5">www.drivesoon-rentals.com</text>
  </svg>
</div>
</body>
</html>
```